Flyer für IT-Dienstleistungen für Privatpersonen
Zielgruppe
IT-Dienstleistungen für Privatpersonen vorwiegened Senioren
Aufgabenstellung
Verwendet werden soll ein DIN A6 Zickzackfalz, Falz Längsseite, Bund Rechts, 6-8Seiten, Matt, Beschnittzugabe 1mm, Sicherheitsabstand 4mm, Farblich und Designtechnisch passend zur Webseite.
Die Textformatierung darf angepasst werden

```html
<!DOCTYPE html>
<html lang="de">
<head>
<meta charset="utf-8">
<title>Flyer IT-Dienstleistungen</title>
<link rel="stylesheet" href="https://fonts.googleapis.com/css2?family=Audiowide&family=Open+Sans:ital,wght@0,300;0,400;1,300&display=swap">
<style>
  :root {
    --stage: #4a4a4a;
    --panel: #262626;
    --panel-dark: #1c1c1c;
    --panel-soft: #3a3a3a;
    --text: #f2f2f2;
    --muted: #c4c4c4;
    --green: #2fb54a;
    --green-deep: #0f6b22;
  }
  * { box-sizing: border-box; margin: 0; padding: 0; }
  html, body { width: 1200px; height: 900px; overflow: hidden; }
  body {
    background: var(--stage);
    font-family: "Open Sans", sans-serif;
    color: var(--text);
  }
  .flyer {
    position: absolute;
    left: 45px; top: 150px;
    width: 1110px; height: 600px;
    display: flex;
    box-shadow: 0 20px 50px rgba(0,0,0,.45);
  }
  .panel {
    position: relative;
    width: 370px; height: 600px;
    padding: 34px 30px;
    background: linear-gradient(160deg, var(--panel-soft) 0%, var(--panel) 45%, var(--panel-dark) 100%);
    overflow: hidden;
  }
  .panel + .panel { border-left: 1px solid rgba(0,0,0,.35); }
  .headline {
    font-family: "Audiowide", sans-serif;
    font-size: 21px;
    line-height: 1.2;
    text-transform: uppercase;
    letter-spacing: .5px;
  }
  .headline .accent { color: var(--green); }
  .service { margin-top: 18px; }
  .service-title {
    font-weight: 300;
    font-size: 12.5px;
    text-transform: uppercase;
    letter-spacing: .4px;
  }
  .service-text {
    font-weight: 300;
    font-size: 10.5px;
    line-height: 1.45;
    color: var(--muted);
    margin-top: 2px;
  }
  .service--boxed {
    background: rgba(255,255,255,.09);
    border-radius: 8px;
    padding: 10px 12px;
    margin-left: -12px; margin-right: -12px;
  }
  .rule { height: 2px; width: 70px; background: var(--green); margin: 22px 0; }
  .rule--long { width: 90px; }

  .glow-top {
    position: absolute; right: -60px; top: -60px;
    width: 220px; height: 220px; border-radius: 50%;
    background: radial-gradient(circle, rgba(47,181,74,.55), transparent 70%);
  }
  .deco-circuit {
    position: absolute; left: 20px; bottom: 40px;
    width: 110px; height: 50px;
    background: linear-gradient(90deg, #8a8a8a, #5a5a5a);
    opacity: .55; border-radius: 6px;
  }
  .deco-molecule {
    position: absolute; right: 30px; bottom: 20px;
    width: 130px; height: 130px; border-radius: 50%;
    background: radial-gradient(circle, #3bd25a 0%, #1a7a2e 55%, transparent 72%);
  }

  .reasons { margin-top: 20px; list-style: none; }
  .reason { display: flex; gap: 12px; margin-bottom: 16px; }
  .reason-icon {
    flex: 0 0 30px; height: 30px; border-radius: 5px;
    background: #6b6b6b;
    display: flex; align-items: center; justify-content: center;
  }
  .contact { margin-top: 34px; }
  .contact-lines { margin-top: 18px; font-weight: 300; font-size: 12px; line-height: 1.6; color: var(--muted); }
  .glow-bottom {
    position: absolute; left: 0; right: 0; bottom: 0; height: 200px;
    background: linear-gradient(180deg, transparent, rgba(20,120,40,.75));
  }
  .deco-monitor {
    position: absolute; right: 28px; bottom: 28px;
    width: 110px; height: 80px; border-radius: 6px;
    background: linear-gradient(135deg, #2a2a2a, #1f8a35);
    border: 4px solid #9a9a9a;
  }
</style>
</head>
<body>
<main class="flyer">

  <section class="panel panel--maintenance">
    <div class="glow-top"></div>
    <h2 class="headline">Wartung und Optimeirung - damit alles <span class="accent">reibungslos</span> läuft.**</h2>

    <div class="service">
      <h3 class="service-title">Dauerhafte Computer-Prüfung</h3>
      <p class="service-text">Ein stabiler und sicherer Computer spart Zeit und Nerven. Wir überprüfen Ihre Geräte jeden Monat, damit alles wie am Schnürchen läuft.</p>
    </div>
    <div class="service">
      <h3 class="service-title">Computer-Optimierung</h3>
      <p class="service-text">Ist Ihr Computer langsam geworden? Wir beschleunigen ihn und sorgen dafür, dass Programme schneller starten und alles wieder Spaß macht.</p>
    </div>
    <div class="service service--boxed">
      <h3 class="service-title">(Neu)Installation und Optimierung</h3>
      <p class="service-text">Ein neuer Computer oder ein frisches Betriebssystem? Wir übernehmen die Einrichtung und passen alles genau nach Ihren Wünschen an.</p>
    </div>

    <div class="deco-circuit" role="img" aria-label="Dekorative Leiterbahnen"></div>
    <div class="deco-molecule" role="img" aria-label="Grüne Netzwerk-Grafik aus verbundenen Knoten"></div>
  </section>

  <section class="panel panel--security">
    <h2 class="headline">Sicherheitslösungen - Ihr Schtz im digitalen Alltag.</h2>
    <div class="service" style="margin-top:30px">
      <h3 class="service-title">Virenscanner</h3>
      <p class="service-text">Wir schützen Sie vor Viren, Betrug und schädlicher Software. Installation, Einrichtung und Lizenz sind inklusive – damit Sie sich keine Sorgen mehr machen müssen.</p>
    </div>
    <div class="rule"></div>
    <h2 class="headline">Mobile Geräte - Ihr Smartphone oder Tablet perfekt einrichten</h2>
    <div class="service">
      <h3 class="service-title">Ersteinrichtung und Datenübertragung</h3>
      <p class="service-text">Ein neues Smartphone oder Tablet kann kompliziert wirken. Wir richten Ihr Gerät ein, übertragen Ihre Daten und installieren alle wichtigen Apps.</p>
    </div>
  </section>

  <section class="panel panel--about">
    <div class="glow-bottom"></div>
    <h2 class="headline" style="margin-top:20px">Warum wir?</h2>
    <div class="rule rule--long" style="margin:8px 0 0 auto"></div>

    <ul class="reasons">
      <li class="reason">
        <span class="reason-icon"><svg width="18" height="18" viewBox="0 0 18 18"><path d="M3 9l4 4 8-8" stroke="#fff" stroke-width="2" fill="none"/></svg></span>
        <div><h3 class="service-title">Ehrlich und transparent:</h3><p class="service-text">Sie zahlen nur das, was Sie wirklich brauchen.</p></div>
      </li>
      <li class="reason">
        <span class="reason-icon"><svg width="18" height="18" viewBox="0 0 18 18"><path d="M3 9l4 4 8-8" stroke="#fff" stroke-width="2" fill="none"/></svg></span>
        <div><h3 class="service-title">Non-Profit:</h3><p class="service-text">Wir handeln bei Privatkunden ohne Gewinnerzielungsabsicht.</p></div>
      </li>
      <li class="reason">
        <span class="reason-icon"><svg width="18" height="18" viewBox="0 0 18 18"><path d="M3 9l4 4 8-8" stroke="#fff" stroke-width="2" fill="none"/></svg></span>
        <div><h3 class="service-title">Verständlich</h3><p class="service-text">Wir erklären Technik in einfachen Worten.</p></div>
      </li>
      <li class="reason">
        <span class="reason-icon"><svg width="18" height="18" viewBox="0 0 18 18"><path d="M3 9l4 4 8-8" stroke="#fff" stroke-width="2" fill="none"/></svg></span>
        <div><h3 class="service-title">Vor Ort oder per Fernwartung:</h3><p class="service-text">Flexibel, wie Sie es wünschen.</p></div>
      </li>
    </ul>

    <div class="contact">
      <h2 class="headline">Kontakiere uns noch heute.</h2>
      <div class="rule rule--long" style="margin:10px 0 0 auto"></div>
      <p class="contact-lines">+49(0) 8631 4407215<br>service@netzobhut.de</p>
    </div>

    <div class="deco-monitor" role="img" aria-label="Monitor mit grüner Doppelhelix-Grafik"></div>
  </section>

</main>
</body>
</html>
```